Creative, Modern and Conversion based Web Design

Kolvex Digital has recently launched a new logo and as part of our companies rebranding, we need a new website aimed towards the UK B2B marketplace.

The website needs to deliver a modern and creative website design whilst ensuring the design is tailored towards conversion optimisation.

This site must drive point of contact either from an online form, via a direct telephone call or Skype connection.

Our sales are all offline so the website will be a simple, elegant and stunning information portal.

Kolvex Digital offers Digital Marketing services to companies throughout the UK - our target audiences are companies that turnover a minimum of 3 million pounds a year and as such we need to deliver a professional image that installs confidence in our companies abilities.

We do not like websites that are reliant upon stock photography - we are happy for stock photography to be used in a small way however the site must not look like a template filled with stock photography.

What do we do

We supply digital marketing services to those companies who demand a strong return on investment - our company prides itself on delivering successful campaigns that help establish long-term profitable relationships.

A lot of the information presented on our old site is relevant today however the design sucks. So please use the information on our current website as a foundation for your design content.

I am looking for several page designs including

"Home Page" Desktop Version
"Service Page" Desktop Version
"Blog Page" Desktop Version

"Home Page" Mobile Version
"Service Page" Mobile Version
"Blog Page" Mobile Version

In the 1st instance please only submit a single design for the "Home Page" Desktop Version - those designers that we are impressed with will be asked to complete the other designs before a winner is selected.

I like modern clean fonts - the site needs to welcome the reader and encourage them to absorb the information - not to overload and make them leave.

The site must be designed to naturally fit our companies new logo.

NO TEMPLATES

Target Market(s)

B2b - 3 million turnover and above

Industry/Entity Type

Digital Marketing

Number of Pages Required

3 page

Requirements
Must have
• Blended well with the companies logo
• We need conversion optimisation to be a huge part of the design - we considered a conversation when a potential customer reaches out to use via - web form, telephone or skype
• The current content on the old website fits today's business but the design sucks.
• www.kolvexdigital-example.com
Nice to have
• We need 3 pages (in 2 variants Desktop and Mobile)
• Home Page
• Service Page
• Blog Page
• Please only deliver the "Home Page" desktop version - if we are happy with your design we will aks for the additional pages
Should not have
• No templates and not stock photo heavy design

```html
<!DOCTYPE html>
<html lang="en">
<head>
<meta charset="utf-8">
<title>Kolvex Digital – Home</title>
<link href="https://fonts.googleapis.com/css2?family=Montserrat:wght@400;500;600;700&family=Open+Sans:wght@400;600&display=swap" rel="stylesheet">
<style>
:root{
  --blue:#1d4f9c;
  --blue-deep:#0f3c85;
  --blue-band:#1a4fa3;
  --ink:#333;
  --muted:#777;
  --soft:#f2f2f2;
  --footer:#2e2e2e;
  --white:#fff;
}
*{margin:0;padding:0;box-sizing:border-box}
html,body{width:1200px;height:2786px;overflow:hidden;background:var(--white)}
body{position:relative;font-family:"Open Sans",Arial,sans-serif;color:var(--ink)}
.abs{position:absolute}
.topline{left:0;top:0;width:1200px;height:3px;background:var(--blue-deep)}
.brand{left:150px;top:30px;display:flex;align-items:center;gap:12px;font-family:"Montserrat",sans-serif;font-weight:700;font-size:26px;color:#555}
.brand-mark{width:36px;height:36px;background:#555}
.call{left:845px;top:14px;display:flex;align-items:center;gap:10px;font-family:"Montserrat",sans-serif;font-weight:600;font-size:15px;color:var(--blue-deep)}
.call-icon{width:40px;height:40px;border:2px solid var(--blue-deep);border-radius:50%;display:flex;align-items:center;justify-content:center}
.nav{left:518px;top:76px;display:flex;gap:0;font-family:"Montserrat",sans-serif;font-size:11.5px;font-weight:600;color:#333}
.nav span{margin-right:46px}
.nav .active{color:var(--blue)}
.hero{left:0;top:103px;width:1200px;height:493px;background:linear-gradient(120deg,#c9b7a6 0%,#7c8aa0 35%,#253b66 70%,#10254c 100%)}
.hero-title{left:150px;top:402px;font-family:"Montserrat",sans-serif;font-size:36px;font-weight:500;color:#1f5bb0}
.hero-sub{left:150px;top:452px;font-family:"Montserrat",sans-serif;font-size:20px;font-weight:500;color:#fff;line-height:32px}
.arrow{top:334px;width:30px;height:30px;border:2px solid #fff;border-radius:50%;display:flex;align-items:center;justify-content:center}
.h2{font-family:"Montserrat",sans-serif;font-weight:600;color:var(--blue-deep)}
.center{left:0;width:1200px;text-align:center}
.intro{font-size:11.5px;line-height:21px;color:var(--muted)}
.card{top:777px;width:272px;height:300px;background:#fff;box-shadow:0 0 10px rgba(0,0,0,.12);text-align:center}
.card .art{width:130px;height:115px;margin:22px auto 0;border-radius:8px;background:linear-gradient(135deg,#f4c542,#4aa3d8)}
.card h3{margin-top:28px;font-family:"Montserrat",sans-serif;font-weight:500;font-size:16px;color:#333}
.card p{margin:16px 22px 0;font-size:11px;line-height:22px;color:var(--muted)}
.band-grey{left:0;top:1142px;width:1200px;height:383px;background:var(--soft)}
.feature h3{font-family:"Montserrat",sans-serif;font-weight:600;font-size:20px;color:var(--blue-deep)}
.feature h4{margin-top:10px;font-family:"Montserrat",sans-serif;font-weight:600;font-size:14.5px;color:var(--blue)}
.feature p{margin-top:28px;font-size:11px;line-height:22.5px;color:#666;text-align:justify}
.btn{display:inline-block;border:2px solid var(--blue);border-radius:20px;font-family:"Montserrat",sans-serif;font-weight:600;font-size:12px;color:var(--blue);padding:11px 22px}
.illus{border-radius:16px}
.about{left:0;top:1902px;width:1200px;height:326px;background:radial-gradient(ellipse at 30% 90%,#2a66c0 0%,var(--blue-band) 45%,#123f8c 100%)}
.about h2{font-family:"Montserrat",sans-serif;font-weight:500;font-size:52px;color:#fff}
.about p{font-size:11.5px;line-height:22px;color:#fff}
.btn-white{border:2px solid #fff;color:#fff;padding:13px 22px;border-radius:24px}
.quote p{font-size:11.5px;line-height:20px;color:#444}
.qmark{font-family:Georgia,serif;font-size:26px;color:#999}
.portrait{left:755px;top:2277px;width:170px;height:170px;border-radius:50%;border:4px solid #ddd;background:linear-gradient(160deg,#6b5a4c,#c7a48a)}
.footer{left:0;top:2508px;width:1200px;height:278px;background:var(--footer)}
.social{top:2532px;width:54px;height:54px;border:1.5px solid #999;border-radius:50%;display:flex;align-items:center;justify-content:center}
.rule{left:150px;width:900px;height:1px;background:#444}
.contact{top:2632px;display:flex;gap:14px;color:#fff}
.contact .ic{width:48px;height:48px;border:1.5px solid #bbb;border-radius:50%;display:flex;align-items:center;justify-content:center;flex:none}
.contact h5{font-family:"Montserrat",sans-serif;font-weight:500;font-size:17px;margin-top:-2px}
.contact p{font-size:11px;line-height:20px;margin-top:2px}
.copy{top:2746px;font-size:11px;color:#ddd}
</style>
</head>
<body>
<div class="abs topline"></div>

<header>
  <div class="abs brand"><span class="brand-mark"></span>Kolvex Digital</div>
  <div class="abs call">
    <span class="call-icon"><svg width="16" height="16" viewBox="0 0 24 24"><path fill="#0f3c85" d="M6.6 10.8a15 15 0 006.6 6.6l2.2-2.2c.3-.3.7-.4 1-.2 1.1.4 2.3.6 3.6.6.6 0 1 .4 1 1V20c0 .6-.4 1-1 1A17 17 0 013 4c0-.6.4-1 1-1h3.5c.6 0 1 .4 1 1 0 1.3.2 2.5.6 3.6.1.3 0 .7-.2 1z"/></svg></span>
    CALL US : (000)-555-0142
  </div>
  <nav class="abs nav"><span class="active">HOME</span><span>ABOUT US</span><span>SERVICES</span><span>WHAT WE DO</span><span>NEWS</span><span>CONTACT US</span></nav>
</header>

<section>
  <div class="abs hero" role="img" aria-label="Photo of a hand touching a glowing digital marketing interface"></div>
  <div class="abs arrow" style="left:113px"><svg width="10" height="12" viewBox="0 0 10 12"><path d="M7 1L2 6l5 5" stroke="#fff" stroke-width="2" fill="none"/></svg></div>
  <div class="abs arrow" style="left:1058px"><svg width="10" height="12" viewBox="0 0 10 12"><path d="M3 1l5 5-5 5" stroke="#fff" stroke-width="2" fill="none"/></svg></div>
  <h1 class="abs hero-title">KOLVEX DIGITAL</h1>
  <p class="abs hero-sub">DIGITAL MARKETING SERVICES<br>TO COMPANIES THROUGHOUT THE UK</p>
</section>

<section>
  <h2 class="abs center h2" style="top:640px;font-size:24px">WHAT WE DO</h2>
  <p class="abs center intro" style="top:683px">Sed ut perspiciatis unde omnis iste natus error sit voluptatem accusantium doloremque laudantium, totam rem aperiam, ab<br>illo inventore veritatis et quasi architecto beatae vitae dicta sunt explicabo.</p>
  <div class="abs card" style="left:150px"><div class="art" role="img" aria-label="Line illustration of email marketing"></div><h3>SED UT PERSPICIATIS</h3><p>Nemo enim ipsam voluptatem quia voluptas sit aspernatur aut odit aut fugit, sed quia consequun tur magni dolores eos qui ratione</p></div>
  <div class="abs card" style="left:464px"><div class="art" role="img" aria-label="Line illustration of analytics dashboard"></div><h3>SED UT PERSPICIATIS</h3><p>Nemo enim ipsam voluptatem quia voluptas sit aspernatur aut odit aut fugit, sed quia consequun tur magni dolores eos qui ratione</p></div>
  <div class="abs card" style="left:778px"><div class="art" role="img" aria-label="Line illustration of creative ideas"></div><h3>SED UT PERSPICIATIS</h3><p>Nemo enim ipsam voluptatem quia voluptas sit aspernatur aut odit aut fugit, sed quia consequun tur magni dolores eos qui ratione</p></div>
</section>

<section>
  <div class="abs band-grey"></div>
  <div class="abs feature" style="left:183px;top:1212px;width:375px">
    <h3>SED UT PERSPICIATIS UNDE</h3>
    <h4>iste natus error sit voluptatem accusantium doloremque</h4>
    <p>Nemo enim ipsam voluptatem quia voluptas sit aspernatur aut odit aut fugit, sed quia consequuntur magni dolores eos qui ratione voluptatem sequi nesciunt. Neque porro quisquam est, qui dolorem ipsum quia dolor sit amet, consectetur, adipisci velit, sed quia non numquam eius modi tempora incidunt ut labore et dolore magnam aliquam quaerat voluptatem.</p>
    <div style="margin-top:28px"><span class="btn">READ MORE</span></div>
  </div>
  <div class="abs illus" style="left:612px;top:1190px;width:360px;height:285px;background:linear-gradient(150deg,#f1d6e0,#9fb8ef 55%,#3f6fd6)" role="img" aria-label="Isometric illustration of a phone with megaphone and growth chart"></div>

  <div class="abs illus" style="left:215px;top:1575px;width:315px;height:285px;background:linear-gradient(150deg,#c8f0e3,#b9c4ef 55%,#5a64c8)" role="img" aria-label="Isometric illustration of a person reviewing a tablet report"></div>
  <div class="abs feature" style="left:625px;top:1585px;width:375px">
    <h3>SED UT PERSPICIATIS UNDE</h3>
    <h4>iste natus error sit voluptatem accusantium doloremque</h4>
    <p>Nemo enim ipsam voluptatem quia voluptas sit aspernatur aut odit aut fugit, sed quia consequuntur magni dolores eos qui ratione voluptatem sequi nesciunt. Neque porro quisquam est, qui dolorem ipsum quia dolor sit amet, consectetur, adipisci velit, sed quia non numquam eius modi tempora incidunt ut labore et dolore magnam aliquam quaerat voluptatem.</p>
    <div style="margin-top:28px"><span class="btn">READ MORE</span></div>
  </div>
</section>

<section>
  <div class="abs about"></div>
  <h2 class="abs center" style="top:1947px;font-family:'Montserrat',sans-serif;font-weight:500;font-size:52px;color:#fff">ABOUT US</h2>
  <p class="abs center" style="top:2033px;font-size:11.5px;line-height:22px;color:#fff">Sed ut perspiciatis unde omnis iste natus error sit voluptatem accusantium doloremque laudantium, totam rem aperiam,<br>eaque ipsa quae ab illo inventore veritatis et quasi architecto beatae vitae dicta sunt explicabo. Nemo enim ipsam volupcon-<br>sequuntur magni dolores eos qui ratione voluptatem sequi nesciunt.</p>
  <div class="abs center" style="top:2127px"><span class="btn btn-white">CLICK HERE FOR MORE INFO</span></div>
</section>

<section>
  <span class="abs qmark" style="left:213px;top:2280px">&ldquo;</span>
  <div class="abs quote" style="left:230px;top:2303px;width:470px"><p>Sed ut perspiciatis unde omnis iste natus error sit voluptatem accusantium doloremque laudantium, totam rem aperiam, eaque ipsa quae ab illo inventore veritatis et quasi architecto beatae vitae dicta sunt explicabo. Nemo enim ipsam voluptatem quia voluptas sit aspernatur aut odit aut fugit, sed quia consequuntur magni dolores eos qui ratione voluptatem sequi nesciunt.</p></div>
  <span class="abs qmark" style="left:566px;top:2375px">&rdquo;</span>
  <div class="abs" style="left:232px;top:2405px;font-family:'Montserrat',sans-serif;font-weight:700;font-size:13px;color:var(--blue)">CLARA WENDT</div>
  <div class="abs" style="left:232px;top:2425px;font-size:11px;color:#666">Posted On 07 Sep 2018</div>
  <div class="abs portrait" role="img" aria-label="Portrait photo of the client giving the testimonial"></div>
</section>

<footer>
  <div class="abs footer"></div>
  <div class="abs social" style="left:416px" aria-label="Social profile"></div>
  <div class="abs social" style="left:480px" aria-label="Social profile"></div>
  <div class="abs social" style="left:541px" aria-label="Social profile"></div>
  <div class="abs social" style="left:605px" aria-label="Social profile"></div>
  <div class="abs social" style="left:666px" aria-label="Social profile"></div>
  <div class="abs social" style="left:730px"><svg width="16" height="12" viewBox="0 0 16 12"><rect x="0.75" y="0.75" width="14.5" height="10.5" fill="none" stroke="#fff" stroke-width="1.5"/><path d="M1 1l7 6 7-6" fill="none" stroke="#fff" stroke-width="1.5"/></svg></div>
  <div class="abs rule" style="top:2607px"></div>

  <div class="abs contact" style="left:180px">
    <span class="ic"><svg width="12" height="17" viewBox="0 0 12 17"><path fill="#fff" d="M6 0a6 6 0 00-6 6c0 4.5 6 11 6 11s6-6.5 6-11a6 6 0 00-6-6zm0 8.2A2.2 2.2 0 116 3.8a2.2 2.2 0 010 4.4z"/></svg></span>
    <div><h5>Address :</h5><p>#4417 Sample Avenue<br>Northfield MO 00000</p></div>
  </div>
  <div class="abs contact" style="left:532px">
    <span class="ic"><svg width="16" height="12" viewBox="0 0 16 12"><rect x="0.75" y="0.75" width="14.5" height="10.5" fill="none" stroke="#fff" stroke-width="1.5"/><path d="M1 1l7 6 7-6" fill="none" stroke="#fff" stroke-width="1.5"/></svg></span>
    <div><h5>Email</h5><p>info@kolvexdigital-example.com</p></div>
  </div>
  <div class="abs contact" style="left:832px">
    <span class="ic"><svg width="16" height="16" viewBox="0 0 24 24"><path fill="#fff" d="M6.6 10.8a15 15 0 006.6 6.6l2.2-2.2c.3-.3.7-.4 1-.2 1.1.4 2.3.6 3.6.6.6 0 1 .4 1 1V20c0 .6-.4 1-1 1A17 17 0 013 4c0-.6.4-1 1-1h3.5c.6 0 1 .4 1 1 0 1.3.2 2.5.6 3.6.1.3 0 .7-.2 1z"/></svg></span>
    <div><h5>Phone</h5><p>Mobile : (000)-555-0142</p></div>
  </div>
  <div class="abs rule" style="top:2720px"></div>
  <p class="abs center copy">© Copyright-2018 Kolvex Digital.All rights reserved</p>
</footer>
</body>
</html>
```